Summer Music/Chorus/Choir Camp for Young Singers Ages 8-13

We need a flyer for a summer camp for young singers ages 8-13. We are nonprofit community children's chorus in Miami, FL. Our camp provides specialized training in music theory, sight-reading,and aural training through daily choral rehearsals in an environment that is both positive and a lot of fun! Our camp offers children the opportunity to come as they are, no matter the level of experience, and grow tremendously in their musicianship skills. In addition to this, our campers participate in song-writing, masterclasses, community performances, and media projects. The final design should be clean, fun, not too crowded, should appeal to boys and girls ages 8-13, and something someone that age would consider "cool" and not too childish. Drawings are cool, something different.
Updates

Target Market(s)

Ages 8-13 and parents of those kids.

Industry/Entity Type

Community

Requirements
Must have
• All info attached.
Nice to have
• Things that relate to music, especially related to singing/choirs
Should not have
• instruments, stock photos of children, or photos from our website (unless they are used very creatively), or photos in general. I've attached our previous camp flyer and our current organization flyer but I don't necessarily want this flyer to look like those.

```html
<!DOCTYPE html>
<html lang="en">
<head>
<meta charset="utf-8">
<title>Summer Camp for Young Singers</title>
<link rel="stylesheet" href="https://fonts.googleapis.com/css2?family=Oswald:wght@400;500&family=Roboto+Condensed:wght@400;500&display=swap">
<style>
  :root {
    --page-bg: #d9d7d4;
    --sheet: #ffffff;
    --ink-white: #ffffff;
    --ink-shadow: rgba(20, 20, 40, 0.75);
    --ink-dark: #2b2b2b;
    --brand-teal: #3f7f86;
    --badge: #1e1e1e;
    --badge-soft: #bdbdbd;
    --sun: #f7c83c;
    --orange: #f39a3c;
    --magenta: #d93d8a;
    --sky: #6cb6e6;
    --royal: #4363c4;
    --mint: #5fc9b5;
  }
  * { box-sizing: border-box; margin: 0; padding: 0; }
  html, body {
    width: 1178px; height: 1200px; overflow: hidden;
    background: var(--page-bg);
  }
  .flyer {
    position: absolute; left: 248px; top: 105px;
    width: 657px; height: 877px;
    background: var(--sheet);
  }
  .artboard {
    position: absolute; left: 12px; top: 12px;
    width: 633px; height: 851px;
    overflow: hidden;
    background:
      radial-gradient(ellipse 55% 35% at 20% 10%, var(--sun), transparent 70%),
      radial-gradient(ellipse 50% 40% at 95% 8%, var(--royal), transparent 70%),
      radial-gradient(ellipse 45% 30% at 55% 45%, var(--sky), transparent 75%),
      radial-gradient(ellipse 35% 30% at 95% 55%, var(--mint), transparent 75%),
      radial-gradient(ellipse 40% 30% at 5% 45%, var(--orange), transparent 70%),
      radial-gradient(ellipse 50% 35% at 15% 85%, var(--magenta), transparent 70%),
      radial-gradient(ellipse 45% 30% at 55% 75%, var(--orange), transparent 75%),
      radial-gradient(ellipse 45% 35% at 95% 85%, var(--sun), transparent 70%),
      linear-gradient(180deg, #f4b86a 0%, #86c2d6 45%, #f08a62 80%, #f3a850 100%);
  }
  .ground {
    position: absolute; left: 0; right: 0; bottom: 0; height: 72px;
    background: var(--sheet);
    border-radius: 40% 40% 0 0 / 18px 18px 0 0;
  }
  .brand {
    position: absolute; left: 14px; top: 18px;
    font-family: "Oswald", sans-serif; font-weight: 500;
    color: var(--brand-teal); line-height: 1;
  }
  .brand-name { font-size: 40px; letter-spacing: 0.5px; }
  .brand-sub { font-size: 20px; margin-top: 4px; padding-left: 120px; }
  .shout, .headline, .subline, .details, .venue {
    font-family: "Oswald", sans-serif; font-weight: 500;
    color: var(--ink-white);
    text-shadow: 1px 2px 3px var(--ink-shadow);
  }
  .shout {
    position: absolute; right: 22px; top: 36px;
    font-size: 27px; letter-spacing: -0.3px;
  }
  .copy {
    position: absolute; left: 63px; width: 555px; top: 150px;
    text-align: center;
  }
  .headline { font-size: 58px; line-height: 62px; letter-spacing: -1.5px; }
  .subline { font-size: 28px; margin-top: 12px; letter-spacing: -0.2px; }
  .details { font-size: 29px; line-height: 48px; margin-top: 24px; letter-spacing: -0.2px; }
  .venue {
    font-family: "Roboto Condensed", sans-serif; font-weight: 500;
    font-size: 20px; line-height: 31px; margin-top: 54px;
  }
  .fine {
    position: absolute; left: 157px; width: 330px; top: 672px;
    text-align: center;
    font-family: "Roboto Condensed", sans-serif; font-size: 12px;
    color: var(--ink-dark); line-height: 18px;
  }
  .fine .fine-main { font-size: 13px; margin-bottom: 6px; }
  .keys-art { position: absolute; left: 0; top: 150px; width: 210px; height: 660px; }
  .keytar-art {
    position: absolute; left: 6px; top: 582px; width: 132px; height: 86px;
    background: linear-gradient(135deg, rgba(60,60,70,0.35), rgba(60,60,70,0.2));
    border-radius: 10px; transform: rotate(-18deg);
  }
  .mic-art {
    position: absolute; left: 492px; top: 74px; width: 138px; height: 52px;
    background: linear-gradient(90deg, rgba(40,40,60,0.35), rgba(40,40,60,0.15));
    border-radius: 26px;
  }
  .sax-art {
    position: absolute; left: 500px; top: 494px; width: 124px; height: 202px;
    background: linear-gradient(180deg, rgba(247,200,60,0.85), rgba(243,154,60,0.85));
    border-radius: 50px 50px 60px 40px;
  }
  .partners {
    position: absolute; top: 790px; left: 0; width: 657px; height: 50px;
  }
  .partner { position: absolute; background: var(--badge); }
  .partner-a { left: 210px; top: 0; width: 50px; height: 50px; }
  .partner-b { left: 292px; top: 3px; width: 100px; height: 44px; }
  .partner-c { left: 418px; top: 13px; width: 170px; height: 22px; background: var(--badge-soft); }
  .footnote {
    position: absolute; left: 0; width: 657px; top: 851px;
    text-align: center;
    font-family: "Roboto Condensed", sans-serif; font-size: 9px; color: #444;
  }
</style>
</head>
<body>
  <main class="flyer">
    <section class="artboard">
      <svg class="keys-art" viewBox="0 0 210 660" role="img" aria-label="Illustration of a winding piano keyboard ribbon in magenta and white">
        <path d="M0 0 C60 40 70 120 40 200 C10 280 40 360 110 430 C170 490 190 580 170 660 L120 660 C140 580 120 500 70 450 C0 380 -20 280 0 200 Z"
              fill="#e05a9c" opacity="0.9"/>
      </svg>
      <div class="keytar-art" role="img" aria-label="Line drawing of a keytar"></div>
      <div class="mic-art" role="img" aria-label="Line drawing of a microphone with cord"></div>
      <div class="sax-art" role="img" aria-label="Line drawing of a saxophone"></div>

      <div class="brand">
        <div class="brand-name">Bright Harmony</div>
        <div class="brand-sub">Chorus</div>
      </div>

      <p class="shout">Register today!</p>

      <div class="copy">
        <h1 class="headline">Summer camp for<br>young singers : ages 8-13</h1>
        <p class="subline">No former music training necessary</p>
        <p class="details">Cost-&nbsp; *$300 for 2-week session<br>July 18-29, 9am-3pm (M-F)*</p>
        <p class="venue">Location<br>Southpoint Cultural Arts Center,<br>4820 SW 180th Street, Miami, FL 33187</p>
      </div>

      <div class="fine">
        <p class="fine-main">*Price does not include lunch."</p>
        <p>*Extended hours available (7:30am-5:30pm) for an extra $50 per week.</p>
      </div>

      <div class="ground"></div>
    </section>

    <div class="partners">
      <span class="partner partner-a"></span>
      <span class="partner partner-b"></span>
      <span class="partner partner-c"></span>
    </div>

    <p class="footnote">Bright Harmony is a 501 (c)(3) Nonprofit organization. Donations made to BHC are tax-exempt."</p>
  </main>
</body>
</html>
```